KV HOLDINGS Business Cards

I need business cards for "KV Holdings group LLC" doublesided... logo on the back (also include logo on front)
logo attached to project... i have jpg up..
Company Info:
418 North Palmer Avenue, Suite 7B
Chicago, Illinois 60654
facsimile 312-555-0187 (list fax, address, website on all cards.)
www.kvholdingsgroup.example
Three different people on cards:
Darnell P. Okafor, CPA MST
Principal
ofc 312-555-0142
mobile 312-555-0169
darnellpokafor@kvholdingsgroup.example
Gregor T. Vanhoutte, CPA MST
Principal
gregortvanhoutte@kvholdingsgroup.example
mobile 708-555-0113
ofc 312-555-0142
Tobias M Quarrie
Principal
ofc 312-555-0142
no mobile
tobiasmquarrie@kvholdingsgroup.example
I have multiple projects listed.. see below:
Business cards for amber ledge partners llc
letterhead
envelopes
Business cards for KV Holdings LLC
letterhead
envelopes
Target Market(s)
rich people
Industry/Entity Type
Business

```html
<!DOCTYPE html>
<html lang="en">
<head>
<meta charset="utf-8">
<title>KV Holdings Group LLC — Business Cards</title>
<link href="https://fonts.googleapis.com/css2?family=Arimo:wght@400;500&display=swap" rel="stylesheet">
<style>
  :root {
    --navy: #1f3566;
    --ink: #2a2d33;
    --card: #f4f4f2;
    --backdrop: #e3e3e0;
    --card-shadow: rgba(20, 28, 45, 0.18);
  }
  * { box-sizing: border-box; margin: 0; padding: 0; }
  html, body {
    width: 1200px;
    height: 900px;
    overflow: hidden;
    background: var(--backdrop);
    font-family: "Arimo", Arial, sans-serif;
  }
  .sheet {
    position: relative;
    width: 1200px;
    height: 900px;
  }
  .card {
    position: absolute;
    left: 320px;
    width: 560px;
    height: 320px;
    background: var(--card);
    box-shadow: 0 6px 18px var(--card-shadow);
    color: var(--navy);
  }
  .card--back { top: 70px; border: 22px solid var(--navy); }
  .card--front { top: 480px; }

  .brand-name {
    font-weight: 400;
    text-transform: uppercase;
    letter-spacing: 0.12em;
    color: var(--navy);
    white-space: nowrap;
  }

  /* back side */
  .back-content {
    height: 100%;
    display: flex;
    flex-direction: column;
    align-items: center;
    justify-content: center;
    gap: 22px;
  }
  .card--back .brand-name { font-size: 26px; }
  .website { font-size: 13px; letter-spacing: 0.02em; color: var(--navy); }

  /* front side */
  .front-frame {
    position: absolute;
    inset: 16px;
    border: 1.5px solid var(--navy);
    padding: 26px 30px 20px;
    display: flex;
    flex-direction: column;
  }
  .card--front .brand-name {
    align-self: center;
    font-size: 16px;
    margin-bottom: 36px;
  }
  .person {
    display: flex;
    align-items: baseline;
    gap: 12px;
    padding-bottom: 6px;
    border-bottom: 1px solid var(--navy);
  }
  .person-name { font-size: 21px; color: var(--navy); }
  .person-title { font-size: 12px; letter-spacing: 0.06em; color: var(--ink); text-transform: uppercase; }
  .contact {
    margin-top: 8px;
    text-align: right;
    font-size: 11.5px;
    line-height: 1.5;
    color: var(--ink);
  }
  .contact .label { color: var(--navy); margin-right: 4px; }
  .contact .sep { color: var(--navy); margin: 0 6px; }
</style>
</head>
<body>
<main class="sheet">

  <section class="card card--back" aria-label="Card back">
    <div class="back-content">
      <p class="brand-name">KV Holdings Group LLC</p>
      <p class="website">www.kvholdingsgroup.example</p>
    </div>
  </section>

  <section class="card card--front" aria-label="Card front">
    <div class="front-frame">
      <p class="brand-name">KV Holdings Group LLC</p>
      <div class="person">
        <span class="person-name">Darnell P. Okafor, CPA MST</span>
        <span class="person-title">Principal</span>
      </div>
      <div class="contact">
        <p>
          <span class="label">T</span>312-555-0142<span class="sep">|</span><span class="label">M</span>312-555-0169<span class="sep">|</span><span class="label">F</span>312-555-0187
        </p>
        <p><span class="label">E</span>darnellpokafor@kvholdingsgroup.example</p>
        <p>418 North Palmer Avenue, Suite 7B</p>
        <p>Chicago, Illinois 60654</p>
      </div>
    </div>
  </section>

</main>
</body>
</html>
```